harvest Soon Book Cover Design for real estate investment book

I am looking for a Book Cover design for my new book. I would like designs for a hardcover, softcover and Lumora book.

The book deals with real estate and mortgage investments. Looking for a clean, bright simple design. Want to cover to be White with big RED letters. See "Dancing past Noon" book for an example ... see attached.

Target Market(s)

Affluent people with money looking for investment solutions.

Industry/Entity Type

Financial Service

Font styles to use
Serif

Requirements
Must have
• Bright clean design that will be appealing to affluent people.
• Title: harvest SOON
• Subtitle: A quiet method for thriving through land holdings
• subsubtitle: Secrets the Bank Teller Keeps Hidden From Clients...
• Author: Ned Falconby
• My Picture on the inside cover or on the back cover
• Book Description, Author description
Nice to have
• Focus on the Front cover look and feel first. Then we can look at the inside flaps and back cover. I will need to send you text. This is for the full cover. Front. Back. Spine. Inside flaps fro hardcover.

```html
<!DOCTYPE html>
<html lang="en">
<head>
<meta charset="utf-8">
<title>harvest SOON — Ned Falconby</title>
<link rel="stylesheet" href="https://fonts.googleapis.com/css2?family=Anton&family=Cinzel:wght@400;500&family=Oswald:wght@700&display=swap">
<style>
  :root {
    --paper: #ecebe9;
    --paper-shade: #dcdbd8;
    --strip: #f1f0ee;
    --red: #e82128;
    --ink: #1c1c1c;
  }
  * { margin: 0; padding: 0; box-sizing: border-box; }
  html, body { width: 848px; height: 1200px; overflow: hidden; background: var(--paper); }
  .cover {
    position: relative;
    width: 848px;
    height: 1200px;
    background: radial-gradient(ellipse at 50% 40%, #f3f2f0 0%, var(--paper) 60%, #e4e3e0 100%);
    overflow: hidden;
  }
  .author {
    position: absolute;
    top: 40px;
    left: 0;
    width: 100%;
    text-align: center;
    font-family: "Cinzel", serif;
    font-weight: 400;
    font-size: 38px;
    letter-spacing: 1px;
    color: var(--ink);
  }
  .title-art { position: absolute; left: 0; top: 0; width: 848px; height: 1200px; }
  .title-word { font-family: "Anton", sans-serif; fill: var(--red); }
  .subtitle { font-family: "Oswald", sans-serif; font-weight: 700; fill: var(--red); }
  .reveal-strip { fill: var(--strip); }
  .reveal-edge { fill: none; stroke: #ffffff; stroke-width: 6; }
  .reveal-text { font-family: "Oswald", sans-serif; font-weight: 700; fill: var(--ink); }
  .building-sketch {
    position: absolute;
    left: 55px;
    top: 886px;
    width: 793px;
    height: 314px;
    background: linear-gradient(180deg, rgba(232,33,40,0.10) 0%, rgba(232,33,40,0.22) 50%, rgba(232,33,40,0.06) 100%);
  }
</style>
</head>
<body>
<main class="cover">
  <p class="author">NED FALCONBY</p>

  <svg class="title-art" viewBox="0 0 848 1200" aria-hidden="false">
    <defs>
      <filter id="strip-shadow" x="-5%" y="-40%" width="110%" height="180%">
        <feDropShadow dx="0" dy="3" stdDeviation="5" flood-color="#000" flood-opacity="0.18"/>
      </filter>
      <linearGradient id="curl" x1="0" y1="0" x2="1" y2="0">
        <stop offset="0" stop-color="#ffffff"/>
        <stop offset="1" stop-color="#cfcecb"/>
      </linearGradient>
    </defs>

    <text class="title-word" x="143" y="355" font-size="250" textLength="623" lengthAdjust="spacingAndGlyphs">HARVEST</text>
    <text class="title-word" x="242" y="583" font-size="250" textLength="428" lengthAdjust="spacingAndGlyphs">SOON</text>

    <text class="subtitle" x="166" y="620" font-size="25" textLength="554" lengthAdjust="spacingAndGlyphs">A QUIET METHOD FOR THRIVING THROUGH LAND HOLDINGS</text>

    <g class="reveal" filter="url(#strip-shadow)">
      <path class="reveal-strip" d="M60 752 L200 748 L360 754 L520 746 L680 752 L848 748 L848 835 L680 829 L520 836 L360 828 L200 835 L60 830 Z"/>
    </g>
    <path class="reveal-edge" d="M60 752 L200 748 L360 754 L520 746 L680 752 L848 748"/>
    <path class="reveal-edge" d="M60 830 L200 835 L360 828 L520 836 L680 829 L848 835"/>
    <rect x="26" y="746" width="46" height="92" rx="22" fill="url(#curl)"/>
    <text class="reveal-text" x="137" y="803" font-size="27" textLength="633" lengthAdjust="spacingAndGlyphs">SECRETS THE BANK TELLER KEEPS HIDDEN FROM CLIENTS...</text>
  </svg>

  <div class="building-sketch" role="img" aria-label="Red line drawing of a modern apartment building with balconies"></div>
</main>
</body>
</html>
```